Agarwood Oud Label Design

I need a circular product label designed for an Agarwood or Bakhoor product. I will provide a rich color scheme picture, as well as the company logo. It may be easier to play with different angles of the logo. So, they are attached also. Label should be 56mm diameter circle label.

```html
<!DOCTYPE html>
<html lang="en">
<head>
<meta charset="utf-8">
<title>Agarwood Oudh Label</title>
<link rel="stylesheet" href="https://fonts.googleapis.com/css2?family=Cinzel:wght@700;900&family=Roboto+Condensed:wght@700&display=swap">
<style>
  :root {
    --page: #ffffff;
    --maroon: #6e1418;
    --maroon-deep: #4a0c0f;
    --gold: #e9c35a;
    --gold-light: #fff0b0;
    --gold-dark: #8a5d14;
    --ink: #2a1408;
  }
  html, body {
    margin: 0;
    padding: 0;
    width: 1200px;
    height: 1200px;
    overflow: hidden;
    background: var(--page);
  }
  .label {
    display: block;
    width: 1200px;
    height: 1200px;
  }
  .brand-name {
    font-family: "Cinzel", serif;
    font-weight: 700;
    font-size: 40px;
    fill: #f4ecdc;
  }
  .product-title {
    font-family: "Cinzel", serif;
    font-weight: 900;
    fill: url(#goldText);
    stroke: var(--maroon-deep);
    stroke-width: 3;
    paint-order: stroke;
  }
  .title-line-1 { font-size: 118px; letter-spacing: 1px; }
  .title-line-2 { font-size: 118px; }
  .net-weight {
    font-family: "Roboto Condensed", sans-serif;
    font-weight: 700;
    font-size: 54px;
    fill: var(--ink);
  }
</style>
</head>
<body>
<svg class="label" viewBox="0 0 1200 1200" xmlns="http://www.w3.org/2000/svg">
  <defs>
    <linearGradient id="goldText" x1="0" y1="0" x2="0" y2="1">
      <stop offset="0" stop-color="#fff3bf"/>
      <stop offset="0.45" stop-color="#e6bb4a"/>
      <stop offset="0.55" stop-color="#b5801f"/>
      <stop offset="1" stop-color="#f2d27a"/>
    </linearGradient>
    <linearGradient id="goldRing" x1="0" y1="0" x2="1" y2="1">
      <stop offset="0" stop-color="#f7df8c"/>
      <stop offset="0.5" stop-color="#a8761c"/>
      <stop offset="1" stop-color="#f1d27c"/>
    </linearGradient>
    <radialGradient id="sceneTone" cx="0.55" cy="0.55" r="0.6">
      <stop offset="0" stop-color="#7a4424"/>
      <stop offset="0.55" stop-color="#4a1a12"/>
      <stop offset="1" stop-color="#26090a"/>
    </radialGradient>
    <linearGradient id="weightPill" x1="0" y1="0" x2="0" y2="1">
      <stop offset="0" stop-color="#fff6d4"/>
      <stop offset="0.5" stop-color="#e7c25a"/>
      <stop offset="1" stop-color="#b88722"/>
    </linearGradient>
  </defs>

  <!-- outer patterned border band -->
  <circle cx="600" cy="600" r="598" fill="var(--maroon-deep)"/>
  <circle cx="600" cy="600" r="556" fill="none" stroke="#8a3a22" stroke-width="72"
          role="img" aria-label="Interlaced geometric knot pattern in gold on maroon"/>
  <circle cx="600" cy="600" r="592" fill="none" stroke="var(--gold-dark)" stroke-width="3"/>
  <circle cx="600" cy="600" r="518" fill="none" stroke="var(--gold-dark)" stroke-width="3"/>

  <!-- gold frame and product scene -->
  <circle cx="600" cy="600" r="510" fill="url(#goldRing)"/>
  <circle cx="600" cy="600" r="500" fill="url(#sceneTone)"
          role="img" aria-label="Photograph of a red perfume bottle with a silver cap, an engraved metal incense box and agarwood chips on red and gold cloth"/>

  <!-- curved Arabic calligraphy -->
  <path class="calligraphy" d="M150 560 A460 460 0 0 1 330 270" fill="none" stroke="#c99a3c" stroke-width="46" stroke-linecap="round" opacity="0.85"
        role="img" aria-label="Arabic calligraphy following the left edge"/>
  <path class="calligraphy" d="M870 270 A460 460 0 0 1 1050 560" fill="none" stroke="#c99a3c" stroke-width="46" stroke-linecap="round" opacity="0.85"
        role="img" aria-label="Arabic calligraphy following the right edge"/>

  <!-- small medallion ornaments -->
  <ellipse cx="150" cy="610" rx="26" ry="32" fill="var(--gold)" role="img" aria-label="Gold arabesque medallion"/>
  <ellipse cx="370" cy="242" rx="30" ry="26" fill="var(--gold)" role="img" aria-label="Gold arabesque medallion"/>
  <ellipse cx="830" cy="242" rx="30" ry="26" fill="var(--gold)" role="img" aria-label="Gold arabesque medallion"/>
  <ellipse cx="1034" cy="610" rx="26" ry="32" fill="var(--gold)" role="img" aria-label="Gold arabesque medallion"/>

  <!-- brand plaque -->
  <g class="brand">
    <ellipse cx="592" cy="208" rx="186" ry="77" fill="url(#goldRing)"/>
    <ellipse cx="592" cy="208" rx="176" ry="68" fill="var(--maroon)"/>
    <text class="brand-name" x="592" y="222" text-anchor="middle">Ember &amp; Grove</text>
  </g>

  <!-- product title -->
  <text class="product-title title-line-1" x="600" y="766" text-anchor="middle" textLength="818" lengthAdjust="spacingAndGlyphs">AGARWOOD</text>
  <text class="product-title title-line-2" x="596" y="882" text-anchor="middle" textLength="405" lengthAdjust="spacingAndGlyphs">OUDH</text>

  <!-- net weight badge -->
  <g class="weight-badge">
    <rect x="409" y="906" width="381" height="149" rx="74.5" fill="url(#goldRing)"/>
    <rect x="415" y="912" width="369" height="137" rx="68.5" fill="var(--maroon)"/>
    <rect x="448" y="936" width="303" height="90" rx="45" fill="var(--gold-dark)"/>
    <rect x="453" y="940" width="293" height="82" rx="41" fill="url(#weightPill)"/>
    <text class="net-weight" x="599" y="1000" text-anchor="middle">50 grams</text>
  </g>
</svg>
</body>
</html>
```